Finance Broker helping people meet their personal and business goals

New business card design,
1st look at the old business card so this makes sense.
I DON'T want:
the subtext "For all your Rural and Commercial Finance".
I DON'T want the: "and Management Consultant" words
I DON'T want the old phone: 07 49217305
I DON'T want the fax number: 07 48160923
I DON'T want the email address: tallowcreek@quarnet.com.au
I DON'T want the flower
What I DO want
I DO want the mobile 0418 365 907 (in larger text)
I DO want:
My name: Dennis Harlow-Pike
I DO want: Australian Credit Licence 512964 (Tallow Creek Pty Ltd)
I DO want: Principal Finance Broker
I DO want new email: dennis@plantreasurepath.com.au
I DO want address: PO Box 836, Innisfail Qld 4860
I DO want the existing logo (PTP on existing card)

Target Market(s)

Business Borrowers, Home Purchasers, and People wanting to finance cars and plant and equipment

Industry/Entity Type

Financial Service

Contact Information for Business Card

See project description

Font styles to use
Serif

Colors

Designer to choose colors to be used in the design.

Requirements
Must have
• See project description
Nice to have
• Black and Yellow colours
Should not have
• See project description

```html
<!DOCTYPE html>
<html lang="en">
<head>
<meta charset="utf-8">
<title>Plan Treasure Path – Business Card</title>
<link rel="stylesheet" href="https://fonts.googleapis.com/css2?family=Tinos:wght@400;700&family=Open+Sans:wght@400;600&display=swap">
<style>
  :root {
    --backdrop: #2a2a2a;
    --card: #111111;
    --yellow: #e8ec6c;
    --white: #ffffff;
    --muted: #e6e6e6;
    --ink: #111111;
  }
  * { box-sizing: border-box; margin: 0; padding: 0; }
  html, body {
    width: 1200px; height: 900px; overflow: hidden;
    background: var(--backdrop);
  }
  .canvas {
    width: 1200px; height: 900px;
    display: flex; flex-direction: column; align-items: center; justify-content: center;
    gap: 56px;
  }
  .card {
    position: relative;
    width: 620px; height: 354px;
    background: var(--card);
    border-radius: 16px;
    overflow: hidden;
    box-shadow: 0 10px 30px rgba(0,0,0,.45);
  }
  .brand {
    position: absolute;
    display: flex; flex-direction: column;
  }
  .brand-row { display: flex; align-items: center; gap: 10px; }
  .brand-name {
    font-family: "Tinos", serif; font-weight: 700;
    color: var(--yellow); font-size: 32px; line-height: 1;
  }
  .brand-dot {
    width: 40px; height: 40px; border-radius: 50%;
    background: var(--yellow);
  }
  .brand-tagline {
    font-family: "Open Sans", sans-serif; color: var(--white);
    font-size: 13px; margin-top: 3px; letter-spacing: .2px;
  }
  .card-front .brand { left: 150px; top: 150px; }

  .card-back .brand { left: 140px; top: 38px; }
  .person {
    position: absolute; left: 0; right: 0; top: 128px;
    text-align: center; font-family: "Tinos", serif; color: var(--white);
  }
  .person-name { font-size: 30px; font-weight: 700; }
  .person-role { font-size: 14px; color: var(--muted); margin-top: 6px; }
  .person-licence { font-size: 14px; color: var(--muted); margin-top: 5px; }
  .person-licence .entity { color: var(--yellow); font-size: 11px; }

  .phone-band {
    position: absolute; left: 0; right: 0; top: 236px; height: 44px;
    background: var(--yellow);
    display: flex; align-items: center; justify-content: center;
    font-family: "Tinos", serif; font-size: 34px; color: var(--ink);
  }
  .contact {
    position: absolute; top: 300px;
    display: flex; align-items: center; gap: 8px;
    font-family: "Tinos", serif; font-size: 15px; color: var(--white);
  }
  .contact svg { width: 14px; height: 14px; flex: none; }
  .contact-email { left: 40px; }
  .contact-address { right: 40px; }
</style>
</head>
<body>
<main class="canvas">
  <section class="card card-front">
    <div class="brand">
      <div class="brand-row">
        <span class="brand-name">Plan Treasure Path</span>
        <span class="brand-dot"></span>
      </div>
      <span class="brand-tagline">A Member of the Tallow Creek Group</span>
    </div>
  </section>

  <section class="card card-back">
    <div class="brand">
      <div class="brand-row">
        <span class="brand-name">Plan Treasure Path</span>
        <span class="brand-dot"></span>
      </div>
      <span class="brand-tagline">A Member of the Tallow Creek Group</span>
    </div>

    <div class="person">
      <div class="person-name">Dennis Harlow-Pike</div>
      <div class="person-role">Principal Finance Broker</div>
      <div class="person-licence">Australian Credit Licence 512964 (<span class="entity">Tallow Creek Pty Ltd</span>)</div>
    </div>

    <div class="phone-band">0418 365 907</div>

    <div class="contact contact-email">
      <svg viewBox="0 0 16 16" aria-hidden="true"><rect x="1" y="3" width="14" height="10" fill="var(--yellow)"/><path d="M1 3 L8 9 L15 3" fill="none" stroke="#111" stroke-width="1.5"/></svg>
      <span>dennis@plantreasurepath.com.au</span>
    </div>
    <div class="contact contact-address">
      <svg viewBox="0 0 16 16" aria-hidden="true"><path d="M8 1a5 5 0 0 0-5 5c0 4 5 9 5 9s5-5 5-9a5 5 0 0 0-5-5z" fill="var(--yellow)"/><circle cx="8" cy="6" r="2" fill="#111"/></svg>
      <span>PO Box 836, Wattlebrook Qld 4872</span>
    </div>
  </section>
</main>
</body>
</html>
```